Luxury Courtside Grove/academy - Webdesign

We want to develop a cutting edge website for a luxury tennis academy. Academy is based in Russia and includes all the necessary amenities for comfortable stay: apartments, spa, tennis courts, training facilities, etc.
We would like to see a clean, simple and modern design (with implementation of all the current trends in web design, although our project has to be distinct and unique).
Color scheme: we would like to see colors present in our logos and all the current associated with tennis. We are open to your ideas and creativity on this front.
The final design should communicate simplicity, be user friendly and convey premium feel.
We woud like to see unique ideas in the design, unconventional techniques, etc.
We don't want standard template design!
Updates
We want to mention that this Tennis Academy has a light focus on nature, as the new material we have uploaded illustrates.
Additional comment to everyone!
We couldn't upload this file to the system: it is too big.
Thank you everyone for your submissions!
Industry/Entity Type
Training
Requirements
Must have
- We would like to see the designs for the following pages:
Home Page:
- Slideshow
- Short description and all the standard stuff
About Us:
- Description with some images
Services:
- Simple description of all of the provided services and possibility to book all of them on the website
! Important ! Develop small system for booking of the days of stay and registration for the courses
Booking and registration !
News:
- Creative layout to display recent news of the academy
Coaches:
- Image and short description of our staff.
Club / Gallery:
- Images and descriptions of the amenities in the territory.
We want a unique display of images: not just lines and rows filled with images
- One idea: an interactive map that displays images and description on mouseover or click on the object on the map (but again, we are open to all your ideas)
Contacts:
- Contact form, contacts, etc.
Sport Store:
- Basic layout for the goods and services provided by the sports store located in the academy
Prices:
- Price lists and ranges with a button leading to registration and booking
For pages like About Us and Services, it would be enough to develop one unified layout for all of them.

```html
<!DOCTYPE html>
<html lang="en">
<head>
<meta charset="utf-8">
<title>Courtside Grove — Tennis Academy</title>
<link rel="stylesheet" href="https://fonts.googleapis.com/css2?family=Ubuntu:ital,wght@0,300;0,400;0,500;1,300;1,400&display=swap">
<style>
  :root {
    --bg-dark: #0b0b0b;
    --green: #2fa84f;
    --green-light: #8dc63f;
    --lime: #d7e72a;
    --yellow: #f2e21c;
    --white: #ffffff;
    --grey-text: #9a9a9a;
    --field: #2a2a2a;
    --divider: #2e2e2e;
  }
  * { box-sizing: border-box; margin: 0; padding: 0; }
  html, body { width: 1200px; height: 750px; overflow: hidden; background: var(--white); }
  body { font-family: "Ubuntu", sans-serif; }
  .page { position: relative; width: 1200px; height: 750px; overflow: hidden; }

  .hero {
    position: absolute; left: 0; top: 0; width: 1200px; height: 632px;
    background: radial-gradient(ellipse at 75% 40%, #1e1e1e 0%, #111 45%, var(--bg-dark) 75%);
    border-bottom: 2px solid var(--green);
  }
  .hero-photo {
    position: absolute; left: 590px; top: 0; width: 610px; height: 632px;
    background:
      radial-gradient(ellipse 22% 20% at 45% 24%, rgba(200,200,200,0.75) 0%, rgba(150,150,150,0.4) 55%, rgba(0,0,0,0) 100%),
      radial-gradient(ellipse 30% 18% at 72% 18%, rgba(170,170,170,0.55) 0%, rgba(110,110,110,0.3) 55%, rgba(0,0,0,0) 100%),
      radial-gradient(ellipse 34% 20% at 68% 50%, rgba(190,190,190,0.6) 0%, rgba(120,120,120,0.3) 55%, rgba(0,0,0,0) 100%),
      radial-gradient(ellipse 26% 45% at 45% 75%, rgba(110,110,110,0.75) 0%, rgba(70,70,70,0.5) 55%, rgba(0,0,0,0) 100%),
      radial-gradient(ellipse 55% 65% at 58% 45%, #4a4a4a 0%, #2a2a2a 45%, rgba(17,17,17,0) 85%);
  }

  .brand { position: absolute; left: 44px; top: 36px; display: flex; align-items: center; gap: 10px; }
  .brand-name { font-weight: 500; font-size: 27px; color: var(--green); letter-spacing: -0.3px; }
  .brand-dot { width: 26px; height: 26px; border-radius: 50%; background: var(--lime); }

  .sidebar { position: absolute; left: 0; top: 128px; width: 194px; height: 472px; border-right: 1px solid var(--divider); }
  .nav-home { position: absolute; left: 45px; top: 21px; }
  .nav { list-style: none; position: absolute; left: 0; top: 49px; width: 194px; }
  .nav li { height: 25.5px; line-height: 21px; padding-left: 45px; font-size: 12px; font-style: italic; font-weight: 300; color: var(--green); }
  .nav li.active {
    margin-left: 24px; padding-left: 21px; color: #111; font-weight: 400;
    background: linear-gradient(90deg, var(--lime), var(--green));
    clip-path: polygon(8px 0, 100% 0, 100% 21px, 0 21px);
    height: 21px; margin-bottom: 4.5px;
  }

  .booking { position: absolute; left: 24px; top: 442px; width: 170px; }
  .booking h2 { margin-left: 21px; font-size: 18px; font-weight: 300; font-style: italic; color: var(--yellow); }
  .field {
    position: relative; height: 22px; margin-top: 9px; background: var(--field);
    clip-path: polygon(8px 0, 100% 0, 100% 100%, 0 100%);
    font-size: 8.5px; font-style: italic; color: #777; line-height: 22px; padding-left: 21px;
  }
  .field:first-of-type { margin-top: 11px; }
  .field-select {
    position: absolute; right: 3px; top: 3px; height: 16px; width: 38px; background: #444;
    color: #ccc; font-size: 7.5px; line-height: 16px; text-align: center;
  }
  .btn-book {
    display: block; margin: 11px 0 0 82px; width: 87px; height: 22px; line-height: 22px;
    background: linear-gradient(90deg, var(--lime), var(--green));
    clip-path: polygon(6px 0, 100% 0, 100% 100%, 0 100%);
    font-size: 12px; font-style: italic; color: #111; text-align: center;
  }

  .intro { position: absolute; left: 254px; top: 134px; width: 300px; }
  .intro h1 { font-size: 33px; font-weight: 300; color: var(--green-light); white-space: nowrap; letter-spacing: -0.3px; }
  .intro h1 span { color: var(--yellow); }
  .lead { margin-top: 22px; width: 296px; font-size: 10.8px; font-style: italic; color: var(--white); line-height: 14px; letter-spacing: -0.1px; }
  .body-text { margin-top: 10px; width: 276px; font-size: 8.7px; font-weight: 300; color: var(--grey-text); line-height: 13.5px; }
  .btn-more {
    display: block; margin-top: 18px; width: 128px; height: 27px; line-height: 27px; padding-left: 28px;
    background: linear-gradient(90deg, var(--lime), var(--green));
    clip-path: polygon(0 0, 100% 0, calc(100% - 10px) 100%, 0 100%);
    font-size: 12.5px; font-style: italic; font-weight: 300; color: #111;
  }

  .news { position: absolute; left: 254px; top: 441px; width: 370px; }
  .news h2 { font-size: 17px; font-weight: 300; color: var(--green-light); }
  .news-item { display: flex; gap: 19px; margin-top: 21px; }
  .news-thumb { width: 57px; height: 57px; background: #3a3a3a; flex: none; }
  .news-text { width: 282px; }
  .news-item h3 { font-size: 10.5px; font-weight: 400; color: var(--white); margin-top: 2px; }
  .news-item p { font-size: 8.4px; font-weight: 300; color: var(--grey-text); line-height: 13.5px; margin-top: 1px; }
  .news-item a { display: block; font-size: 8px; font-style: italic; color: var(--yellow); text-decoration: none; line-height: 12px; }

  .slide-prev { position: absolute; left: 1028px; top: 524px; }
  .slide-next { position: absolute; left: 1104px; top: 509px; width: 81px; height: 81px; background: #2a2a2a; display: flex; align-items: center; justify-content: center; }

  .scroll-down { position: absolute; left: 585px; top: 617px; }
</style>
</head>
<body>
<div class="page">
  <section class="hero">
    <div class="hero-photo" role="img" aria-label="Black and white photo of a tennis player holding a racket ready for a backhand"></div>

    <div class="brand">
      <span class="brand-name">Courtside Grove</span>
      <span class="brand-dot"></span>
    </div>

    <aside class="sidebar">
      <svg class="nav-home" width="15" height="14" viewBox="0 0 15 14" aria-label="Home">
        <path d="M7.5 0 L15 7 H12.5 V14 H9 V9.5 H6 V14 H2.5 V7 H0 Z" fill="#f2e21c"/>
      </svg>
      <ul class="nav">
        <li>About us</li>
        <li>Services</li>
        <li class="active">Booking &amp; Registration</li>
        <li>News</li>
        <li>Coaches</li>
        <li>Club Gallery</li>
        <li>Contacts</li>
        <li>Sport Store</li>
        <li>Prices</li>
      </ul>
    </aside>

    <form class="booking">
      <h2>Booking</h2>
      <div class="field">Your name here</div>
      <div class="field">Date you want to book<span class="field-select">select</span></div>
      <span class="btn-book">Book me!</span>
    </form>

    <div class="intro">
      <h1>Welcome on <span>Courtside Grove!</span></h1>
      <p class="lead">Lorem ipsum dolor sit amet, consectetur adipiscing elit. Etiam ut nibh dolor. Vivamus ac lacus ipsum, a pretium magna.</p>
      <p class="body-text">Integer porttitor lorem eu orci dictum pharetra. Suspendisse diam nisi, malesuada vel faucibus id, pretium eget nulla. Nulla iaculis, magna a feugiat dapibus, odio magna auctor dui, eu suscipit velit urna scelerisque purus. In pharetra feugiat massa ac tincidunt. In hac habitasse platea dictumst.</p>
      <span class="btn-more">Read More</span>
    </div>

    <div class="news">
      <h2>What’s new?</h2>
      <article class="news-item">
        <div class="news-thumb"></div>
        <div class="news-text">
          <h3>Suspendisse ac lorem fermentum</h3>
          <p>metus commodo consequat ac in velit. Aliquam iaculis consectetur aliquet. Vestibulum semper interdum massa, nec semper velit faucibus in.</p>
          <a href="#">read more &gt;&gt;</a>
        </div>
      </article>
    </div>

    <svg class="slide-prev" width="34" height="52" viewBox="0 0 34 52" aria-label="Previous slide">
      <polyline points="30,3 6,26 30,49" fill="none" stroke="#555" stroke-width="5"/>
    </svg>
    <div class="slide-next">
      <svg width="34" height="52" viewBox="0 0 34 52" aria-label="Next slide">
        <polyline points="4,3 28,26 4,49" fill="none" stroke="#8dc63f" stroke-width="5"/>
      </svg>
    </div>
  </section>

  <svg class="scroll-down" width="30" height="30" viewBox="0 0 30 30" aria-label="Scroll down">
    <circle cx="15" cy="15" r="14" fill="#fff" stroke="#2fa84f" stroke-width="2"/>
    <circle cx="15" cy="15" r="10" fill="#2fa84f"/>
    <path d="M13.5 9 H16.5 V14 H19 L15 19 L11 14 H13.5 Z" fill="#fff"/>
  </svg>
</div>
</body>
</html>
```